Drifting Pelican Coffee Co menu

We would like our existing menu tidied up.
we want to keep the all the items, but need it less busy and clearer to read.

Also want to leave a bit of space to add a few item in the future.

```html
<!DOCTYPE html>
<html lang="en">
<head>
<meta charset="utf-8">
<title>Drifting Pelican Coffee Co — Menu</title>
<link rel="stylesheet" href="https://fonts.googleapis.com/css2?family=Rye&family=Oswald:wght@500&family=Montserrat:wght@400;600;700&display=swap">
<style>
:root{
  --backdrop:#e9e8e1;
  --paper-light:#dcbf9f;
  --paper-dark:#c9a27f;
  --ink:#231a15;
  --rust:#8a3219;
  --pill-dark:#1b1512;
  --panel:#e4e3db;
  --leaf-dark:#3f6b4a;
  --leaf-light:#8fb08f;
  --rule:#6a5443;
}
*{box-sizing:border-box;margin:0;padding:0}
html,body{width:1200px;height:1085px;overflow:hidden}
body{background:var(--backdrop);font-family:"Montserrat",sans-serif;color:var(--ink)}
.menu{position:absolute;left:0;top:118px;width:1200px;height:848px;
  background:radial-gradient(ellipse at 40% 40%,var(--paper-light),var(--paper-dark));overflow:hidden}
.abs{position:absolute;z-index:1}

.brand{left:34px;top:40px;width:230px;display:flex;align-items:center;gap:10px}
.brand__dot{width:14px;height:14px;border-radius:50%;background:var(--ink);flex:none}
.brand__name{font-family:"Rye",serif;font-size:19px;line-height:1.15;color:var(--ink)}

.title{font-family:"Rye",serif;color:var(--ink);text-align:center;line-height:1;font-weight:400}
.title__main{font-size:40px;display:block}
.title__sub{font-size:22px;display:block;margin-top:2px}
.title--coffee{left:330px;top:34px;width:210px}
.title--iced{left:720px;top:34px;width:340px;background:var(--paper-light);padding:0 10px;z-index:2}

.iced-frame{left:601px;top:66px;width:571px;height:444px;border:1px solid var(--rule)}

.heading{font-family:"Oswald",sans-serif;font-weight:500;color:var(--rust);font-size:27px;letter-spacing:.5px;line-height:1;white-space:nowrap}

.col{display:flex;flex-direction:column}
.item-line{display:flex;align-items:baseline;font-weight:600;font-size:10.5px;text-transform:uppercase;letter-spacing:.2px;white-space:nowrap}
.leader{flex:1;border-bottom:1.2px dotted var(--ink);margin:0 4px;transform:translateY(-3px);min-width:6px}
.price{font-weight:600;font-size:11.5px;text-transform:none}
.desc{font-size:8.6px;line-height:1.3;margin-top:2px;max-width:170px}
.sizes{display:flex;gap:3px;margin-top:5px}
.pill{background:var(--pill-dark);color:#fff;font-size:8.4px;font-weight:600;padding:2px 7px;border-radius:9px}
.pill--mid{background:var(--rust)}

.coffee{left:60px;top:162px;width:222px;gap:12px}
.coffee .heading{margin-bottom:4px}
.tea{left:328px;top:164px;width:214px;gap:13px}
.tea .heading{margin-bottom:4px;letter-spacing:0}
.tea-extras{left:328px;top:509px;width:214px;border-top:1px solid var(--rule);padding-top:18px}
.extra-title{font-size:10px;font-weight:600;text-transform:uppercase}
.extra-list{font-size:8.6px;margin-top:8px;text-transform:uppercase;line-height:1.3}
.extra-price{color:var(--rust);font-size:11.5px;margin-top:8px;margin-bottom:18px}

.iced{left:644px;top:162px;width:213px;gap:9px}
.iced .heading{margin-bottom:6px}
.iced .desc{margin-top:3px}
.iced-rule{left:644px;top:324px;width:213px;border-top:1px solid var(--rule)}
.other{left:644px;top:358px;width:213px;gap:14px}
.other .heading{margin-bottom:2px}
.shakes{left:925px;top:162px;width:197px;gap:15px}
.shakes .intro{font-size:10px;font-weight:600;line-height:1.25;margin-top:7px;margin-bottom:-3px}

.box{border:1px solid var(--rule);padding:14px 14px 10px}
.box--chai{left:61px;top:694px;width:250px;height:128px}
.box--cacao{left:327px;top:694px;width:248px;height:128px}
.box-head{display:flex;align-items:flex-start;gap:8px;color:var(--rust);font-weight:700;font-size:10px;text-transform:uppercase;line-height:1.2}
.tag{background:var(--pill-dark);color:#fff;font-size:8.6px;font-weight:600;padding:2px 7px;border-radius:9px;white-space:nowrap}
.box .desc{max-width:none;margin-top:9px;font-size:8.4px}

.specialty{left:586px;top:509px;width:614px;height:339px;background:var(--panel)}
.specialty__title{position:absolute;left:47px;top:42px;font-family:"Rye",serif;font-size:30px;color:var(--ink);font-weight:400}
.special{position:absolute;width:215px}
.special .desc{max-width:none;font-size:8.4px;margin-top:8px}
.special--a{left:56px;top:100px}
.special--b{left:299px;top:100px}
.special--c{left:56px;top:190px}
.special--d{left:299px;top:190px}

.foliage{position:absolute;z-index:0;background:linear-gradient(160deg,var(--leaf-light),var(--leaf-dark));opacity:.75;border-radius:40% 10% 40% 10%}
.foliage--top{left:1140px;top:0;width:60px;height:66px}
.foliage--right{left:1162px;top:520px;width:38px;height:230px;z-index:2}
.foliage--left{left:0;top:690px;width:48px;height:158px}
.foliage--edge1{left:0;top:230px;width:10px;height:90px}
.foliage--edge2{left:0;top:350px;width:26px;height:80px}
</style>
</head>
<body>
<main class="menu">
  <div class="abs brand"><span class="brand__dot"></span><span class="brand__name">Drifting Pelican Coffee Co</span></div>

  <h1 class="abs title title--coffee"><span class="title__main">COFFEE</span><span class="title__sub">&amp; TEA</span></h1>

  <div class="abs iced-frame"></div>
  <h1 class="abs title title--iced"><span class="title__main">ICED COFFEE</span><span class="title__sub">&amp; Milkshakes</span></h1>

  <section class="abs col coffee">
    <h2 class="heading">COFFEE</h2>
    <div class="item"><div class="item-line"><span>Flat White</span><span class="leader"></span><span class="price">$5.00</span></div><p class="desc">Espresso shot with a steamed milk.</p><div class="sizes"><span class="pill">Small $5</span><span class="pill pill--mid">Medium $6</span><span class="pill">Large $7</span></div></div>
    <div class="item"><div class="item-line"><span>Cappuccino</span><span class="leader"></span><span class="price">$5.00</span></div><p class="desc">Espresso shot with steamed milk, a thick layer of milk foam and chocolate powder topping</p><div class="sizes"><span class="pill">Small $5</span><span class="pill pill--mid">Medium $6</span><span class="pill">Large $7</span></div></div>
    <div class="item"><div class="item-line"><span>Latte</span><span class="leader"></span><span class="price">$5.00</span></div><p class="desc">Espresso shot with steamed milk and a thin layer of milk foam</p><div class="sizes"><span class="pill">Small $5</span><span class="pill pill--mid">Medium $6</span><span class="pill">Large $7</span></div></div>
    <div class="item"><div class="item-line"><span>Mocha</span><span class="leader"></span><span class="price">$5.00</span></div><p class="desc">Espresso shot, Belgian chocolate RAW natural infusion with a medium layer of milk foam.</p><div class="sizes"><span class="pill">Small $5</span><span class="pill pill--mid">Medium $6</span><span class="pill">Large $7</span></div></div>
    <div class="item"><div class="item-line"><span>Americano</span><span class="leader"></span><span class="price">$5.00</span></div><p class="desc"><b>Americano</b> - Espresso shot topped up with hot water.<br><b>Long Black</b> - Hot water topped off with espresso shot</p><div class="sizes"><span class="pill">Small $5</span><span class="pill pill--mid">Medium $6</span><span class="pill">Large $7</span></div></div>
    <div class="item"><div class="item-line"><span>Espresso</span><span class="leader" style="border:0"></span><span class="price">$3.00</span></div><p class="desc">Double espresso shot</p></div>
    <div class="item"><div class="item-line"><span>Filter / Batch Brew Coffee</span><span class="leader" style="border:0"></span><span class="price">$4.00</span></div><div class="sizes"><span class="pill">Small $4</span><span class="pill pill--mid">Medium $4</span><span class="pill">Large $4</span></div></div>
  </section>

  <section class="abs col tea">
    <h2 class="heading">TEA / OTHER DRINKS</h2>
    <div class="item"><div class="item-line"><span>Organic Green Tea</span><span class="leader"></span><span class="price">$5.00</span></div><div class="sizes"><span class="pill">Small $5</span><span class="pill pill--mid">Medium $6</span><span class="pill">Large $7</span></div></div>
    <div class="item"><div class="item-line"><span>English Breakfast Tea</span><span class="leader"></span><span class="price">$5.00</span></div><div class="sizes"><span class="pill">Small $5</span><span class="pill pill--mid">Medium $6</span><span class="pill">Large $7</span></div></div>
    <div class="item"><div class="item-line"><span>Organic Earl Grey Tea</span><span class="leader"></span><span class="price">$5.00</span></div><div class="sizes"><span class="pill">Small $5</span><span class="pill pill--mid">Medium $6</span><span class="pill">Large $7</span></div></div>
    <div class="item"><div class="item-line"><span>Hot Chocolate</span><span class="leader"></span><span class="price">$5.00</span></div><div class="sizes"><span class="pill">Small $5</span><span class="pill pill--mid">Medium $6</span><span class="pill">Large $7</span></div></div>
    <div class="item"><div class="item-line"><span>Dark Cacoa Hot Chocolate</span><span class="leader" style="border:0;margin:0 2px"></span><span class="price">$5.00</span></div><div class="sizes"><span class="pill">Small $5</span><span class="pill pill--mid">Medium $6</span><span class="pill">Large $7</span></div></div>
    <div class="item"><div class="item-line"><span>Chai Latte</span><span class="leader"></span><span class="price">$5.00</span></div><div class="sizes"><span class="pill">Small $5</span><span class="pill pill--mid">Medium $6</span><span class="pill">Large $7</span></div></div>
  </section>

  <section class="abs tea-extras">
    <h3 class="extra-title">Raw Natural Infusions</h3>
    <p class="extra-list">Caramel, Vanilla, Chai Spice,<br>Hazelnut, Belgian Chocolate</p>
    <p class="extra-price">$5.00</p>
    <h3 class="extra-title">Milks</h3>
    <p class="extra-list">Full Cream, Skinny, Oat,<br>Almond, Soy</p>
    <p class="extra-price">$5.00</p>
  </section>

  <section class="abs col iced">
    <h2 class="heading">ICED COFFEE</h2>
    <div class="item"><div class="item-line"><span>Iced Latte</span><span class="leader"></span><span class="price">$7.50</span></div><p class="desc">Add icecream + $1.00</p></div>
    <div class="item"><div class="item-line"><span>Iced Mocha</span><span class="leader"></span><span class="price">$8.00</span></div><p class="desc">Add icecream + $1.00</p></div>
    <div class="item"><div class="item-line"><span>Iced Americano</span><span class="leader"></span><span class="price">$6.00</span></div></div>
    <div class="item"><div class="item-line"><span>Cold Brew</span><span class="leader"></span><span class="price">$7.50</span></div></div>
  </section>
  <div class="abs iced-rule"></div>
  <section class="abs col other">
    <h2 class="heading">OTHER DRINKS</h2>
    <div class="item-line"><span>Iced Chocolate</span><span class="leader"></span><span class="price">$7.00</span></div>
    <div class="item-line"><span>Iced Chai</span><span class="leader"></span><span class="price">$7.00</span></div>
    <div class="item-line"><span>Puppycino</span><span class="leader"></span><span class="price">$2.00</span></div>
  </section>

  <section class="abs col shakes">
    <h2 class="heading">MILKSHAKES</h2>
    <p class="intro">Milkshake with a choice of chilled milk and ice cream</p>
    <div class="item-line"><span>Chocolate</span><span class="leader"></span><span class="price">$8.00</span></div>
    <div class="item-line"><span>Vanilla</span><span class="leader"></span><span class="price">$8.00</span></div>
    <div class="item-line"><span>Caramel</span><span class="leader"></span><span class="price">$8.00</span></div>
    <div class="item-line"><span>Strawberry</span><span class="leader"></span><span class="price">$8.00</span></div>
    <div class="item-line"><span>Mango</span><span class="leader"></span><span class="price">$8.00</span></div>
    <div class="item-line"><span>Banana</span><span class="leader"></span><span class="price">$8.00</span></div>
    <div class="item-line"><span>Cookies &amp; Cream</span><span class="leader"></span><span class="price">$8.00</span></div>
    <div class="item-line"><span>Hazelora Milkshake</span><span class="leader"></span><span class="price">$9.00</span></div>
  </section>

  <section class="abs box box--chai">
    <div class="box-head"><span>Honey Brewed Chai</span><span class="tag">$7.00</span></div>
    <p class="desc">Our Honey Chai is handmade and blended in Western Australia. It is made from the finest black tea leaves available, aromatic freshly ground spices and infused with locally sourced raw honey. Served with a choice of steamed milk</p>
  </section>
  <section class="abs box box--cacao">
    <div class="box-head"><span>Colombian Cacoa Salted Caramel Hot Chocolate</span><span class="tag">$7.00</span></div>
    <p class="desc" style="margin-top:5px">Made with deep toned and rich cocoa sourced from ancient cocao growing regions of Colombia and sweetened with just enough organic unrefined Colombian panela, all balanced perfectly with a caramel RAW natural infusion and pink Himalayan rock salt. Served with a choice of steamed milk</p>
  </section>

  <section class="abs specialty">
    <h2 class="specialty__title">SPECIALTY DRINKS</h2>
    <div class="special special--a"><div class="box-head"><span>Spicecrumb Iced Coffee</span><span class="tag">$9.00</span></div><p class="desc">A double shot of espresso extracted over Spicecrumb spread poured over Brookvale premium extra creamy milk and ice cream. Topped off with whipped cream and crushed Spicecrumb cookies</p></div>
    <div class="special special--b"><div class="box-head"><span>Hazelora Iced Coffee</span><span class="tag">$9.00</span></div><p class="desc">A double shot of espresso extracted over melted Hazelora poured over Brookvale premium extra creamy milk and ice cream. Topped off with whipped cream and more Hazelora sauce and crushed Hazelnuts</p></div>
    <div class="special special--c"><div class="box-head"><span>Maltibites Iced Coffee</span><span class="tag">$9.00</span></div><p class="desc">A double shot of espresso extracted over melted Maltibites poured over Brookvale premium extra creamy milk and ice cream. Topped off with whipped cream and more crushed Maltibites</p></div>
    <div class="special special--d"><div class="box-head"><span>Colombian Cacoa Salted Caramel Milkshake</span><span class="tag">$9.00</span></div><p class="desc" style="margin-top:5px">Made with deep toned and rich cocoa sourced from ancient cocoa growing regions of Colombia and sweetened with just enough organic unrefined Colombian panela, all balanced perfectly with a caramel RAW natural infusion and pink Himalayan rock salt. All blended together with icecream and a choice of milk</p></div>
  </section>

  <div class="foliage foliage--top" role="img" aria-label="Illustrated coffee leaves"></div>
  <div class="foliage foliage--right" role="img" aria-label="Illustrated coffee branch with leaves and red cherries"></div>
  <div class="foliage foliage--left" role="img" aria-label="Illustrated coffee leaves and cherries"></div>
  <div class="foliage foliage--edge1" role="img" aria-label="Illustrated leaf edge"></div>
  <div class="foliage foliage--edge2" role="img" aria-label="Illustrated leaf edge"></div>
</main>
</body>
</html>
```